Book cover design for 'Lantern Winter' novel

Title of book 'Lantern Winter'
Subtitle 'a Ness Orford novel'
Author 'T K Halvorsen'
Book genre 'novel - adventure'
Format ' eBook, paperback, audio, thumbnail'
Type 'Self-publishing through PVL'
Trim size 6 x 9
Back cover 'Seeking redemption on the Via de la Plata.
Ness Orford’s life changed forever in a moment of madness. Haunted by his crime, Ness feels a calling to seek redemption on the Camino de Santiago.
The daily toil of walking the Via de la Plata from Seville causes Ness to search his soul.
On The Way Ness encounters other pilgrims with their own personal reasons to answer the call of the camino.
Join Ness for the many highs and lows of camino life as he moves step by step closer to his goal.
Can the Camino give Ness peace of mind and stop his nightmares?'
Overall vision 'The front cover at the top should be the title:
Camino
Calling
This will fill about 20 per cent of the front cover. It must be centre justified. The title should use the same type face as the official Camino de Santiago road sign (see first download). The type should be in bright blue. The background should be in bright yellow.
Under the title should be an image of a path stretching to the horizon with the shadow of a pilgrim (see second download).
Superimposed on the image should be the words 'a Ness Orford novel' maybe using a type face similar to the street signage used in Spain (see third download).
At the bottom of the front cover should be the author's name 'Tom Halvorsen' in the same style as the blue and yellow title - BUT MUCH SMALLER.
On the SPINE of the book should be 'Lantern Winter' and 'Tom Halvorsen' in the blue text on yellow background.
On the back cover there should be a photograph (see fourth download) with the text UPDATE ON THE TEXT 'Seeking redemption on the Via de la Plata.
In a moment of madness Ness Orford’s life changed forever. Haunted by his atrocious act, he feels a calling to seek redemption on the Camino de Santiago.
The daily slog of walking the Via de la Plata from Seville causes Ness to search deep within his soul.
On The Way Ness encounters other pilgrims with their own personal reasons to answer the call of the Camino.
Can the Camino give Ness peace of mind and stop his nightmares?' with a three centimetre space at the bottom for bar code/ISBN and the author headshot photograph attached.

Target Market(s)

Readers who have walked the Camino de Santiago in Spain or who are interested

Requirements
Nice to have
• I would like my headshot (attached) included on the back cover

```html
<!DOCTYPE html>
<html lang="en">
<head>
<meta charset="utf-8">
<title>Lantern Winter – Cover Wrap</title>
<link rel="stylesheet" href="https://fonts.googleapis.com/css2?family=Archivo+Black&family=Nunito:wght@800&family=Rye&display=swap">
<style>
  :root {
    --title-blue: #3bb3e8;
    --shadow-ink: #1f2a33;
    --spine-yellow: #fbf730;
    --sun-yellow: #fff64a;
    --dust-orange: #e99a2a;
    --sky-grey: #c9ccd2;
    --meadow-green: #6f8a4a;
    --track-sand: #b59a76;
    --white: #ffffff;
  }
  * { margin: 0; padding: 0; box-sizing: border-box; }
  html, body { width: 1200px; height: 840px; overflow: hidden; background: #ffffff; }
  .cover-wrap { position: relative; width: 1200px; height: 840px; overflow: hidden; }

  /* Back cover */
  .back-cover { position: absolute; left: 0; top: 0; width: 559px; height: 840px; }
  .back-photo {
    position: absolute; inset: 0;
    background: linear-gradient(180deg, var(--sky-grey) 0%, #dcdde0 30%, #a6ad8e 36%, var(--meadow-green) 52%, #8b8a5c 70%, var(--track-sand) 100%);
  }
  .blurb {
    position: absolute; left: 49px; top: 43px; width: 482px;
    font-family: "Nunito", Arial, sans-serif; font-weight: 800;
    font-size: 14.4px; line-height: 17.3px; letter-spacing: -0.35px;
    color: var(--white);
    text-shadow: 0 0 2px #000, 1px 1px 1px #000;
    text-align: justify;
  }
  .blurb p { margin: 0; }
  .blurb .tagline { margin-bottom: 17px; }
  .blurb .indent { text-indent: 50px; }

  /* Spine */
  .spine { position: absolute; left: 559px; top: 0; width: 79px; height: 840px; background: var(--spine-yellow); }
  .spine-text {
    position: absolute; left: 50%; white-space: nowrap;
    font-family: "Archivo Black", Arial, sans-serif; font-size: 25px;
    color: var(--title-blue);
    transform: translate(-50%, -50%) rotate(-90deg);
  }
  .spine-author { top: 213px; }
  .spine-title { top: 648px; }

  /* Front cover */
  .front-cover { position: absolute; left: 638px; top: 0; width: 562px; height: 840px; overflow: hidden; }
  .front-art {
    position: absolute; inset: 0;
    background:
      radial-gradient(ellipse 90px 520px at 64% 100%, rgba(255,248,120,0.95), rgba(255,248,120,0) 100%),
      linear-gradient(180deg, #fff84a 0%, var(--sun-yellow) 40%, #efe24a 46%, #e2b43a 55%, var(--dust-orange) 75%, #e8872a 100%);
  }
  .front-title {
    position: absolute; left: 0; top: 44px; width: 562px; text-align: center;
    font-family: "Archivo Black", Arial, sans-serif; font-size: 108px; line-height: 88px;
    letter-spacing: 2px; color: var(--title-blue);
    text-shadow: 4px 4px 0 var(--shadow-ink);
  }
  .series-line {
    position: absolute; left: 0; top: 414px; width: 562px; text-align: center;
    font-family: "Rye", Georgia, serif; font-size: 27px; letter-spacing: 0.5px;
    color: var(--white); text-transform: uppercase;
    text-shadow: 1px 1px 2px rgba(0,0,0,0.35);
  }
  .front-author {
    position: absolute; left: 0; top: 762px; width: 562px; text-align: center;
    font-family: "Archivo Black", Arial, sans-serif; font-size: 33px;
    color: var(--white);
    text-shadow: 2px 2px 2px rgba(80,50,0,0.4);
  }
</style>
</head>
<body>
<div class="cover-wrap">

  <section class="back-cover">
    <div class="back-photo" role="img" aria-label="Photograph of a dirt pilgrim track through green meadow under a grey sky, with a stone Via de la Plata waymarker bearing the scallop shell and yellow arrow in the foreground"></div>
    <div class="blurb">
      <p class="tagline">Seeking redemption on the Via de la Plata.</p>
      <p class="indent">Ness Orford’s life changed forever in a moment of madness. Haunted by his crime, Ness feels a calling to seek redemption on the Camino de Santiago.</p>
      <p>The daily toil of walking the Via de la Plata from Seville causes Ness to search his soul.</p>
      <p class="indent">On The Way Ness encounters other pilgrims with their own personal reasons to answer the call of the camino.</p>
      <p class="indent">Join Ness for the many highs and lows of camino life as he moves step by step closer to his goal.</p>
      <p>Can the Camino give Ness peace of mind and stop his nightmares?</p>
    </div>
  </section>

  <section class="spine">
    <div class="spine-text spine-author">T K Halvorsen</div>
    <div class="spine-text spine-title">Lantern Winter</div>
  </section>

  <section class="front-cover">
    <div class="front-art" role="img" aria-label="Sun-washed yellow and orange landscape with a straight path stretching to distant hills and the long shadow of a pilgrim on the path"></div>
    <h1 class="front-title">Lantern<br>Winter</h1>
    <p class="series-line">A Ness Orford Novel</p>
    <p class="front-author">T K Halvorsen</p>
  </section>

</div>
</body>
</html>
```